Business Card Design

Business card design.

Business card is to have logo, website address and email address.

Website is www.brightkettle.ie
Email is info@brightkettle.ie
Logo uploaded

I have ordered Business Card Printing via Print Harbor, the Double-sided colour printed option with gloss finish.

Industry/Entity Type

Business

```html
<!DOCTYPE html>
<html lang="en">
<head>
<meta charset="utf-8">
<title>Bright Kettle – Business Cards</title>
<link rel="stylesheet" href="https://fonts.googleapis.com/css2?family=Fira+Sans:wght@300;700&display=swap">
<style>
  :root {
    --stage-dark: #0b0b0b;
    --stage-mid: #6e6f72;
    --stage-light: #d9dadc;
    --card-white: #ffffff;
    --brand-red: #ec1c24;
    --brand-red-deep: #b3121a;
    --ink: #1b1b1b;
    --grey-top: #7a7b7e;
    --grey-bottom: #050505;
  }
  * { margin: 0; padding: 0; box-sizing: border-box; }
  html, body { width: 1200px; height: 900px; overflow: hidden; }
  body {
    position: relative;
    background: linear-gradient(90deg, var(--stage-dark) 0%, var(--stage-mid) 22%, var(--stage-light) 50%, var(--stage-mid) 78%, var(--stage-dark) 100%);
    font-family: "Fira Sans", Arial, sans-serif;
  }
  .card {
    position: absolute;
    left: 270px;
    width: 660px;
    height: 426px;
    overflow: hidden;
  }
  .card--front { top: 15px; }
  .card--back { top: 457px; }
  .card__shape { position: absolute; inset: 0; width: 660px; height: 426px; }
  .brand {
    position: absolute;
    left: 0;
    width: 490px;
    top: 98px;
    display: flex;
    align-items: center;
    justify-content: center;
    gap: 12px;
  }
  .brand__dot {
    width: 40px; height: 40px;
    border-radius: 50%;
    background: var(--brand-red);
  }
  .brand__name {
    font-weight: 700;
    font-size: 40px;
    letter-spacing: 0.5px;
    color: var(--ink);
  }
  .contact {
    position: absolute;
    left: 278px;
    top: 290px;
    list-style: none;
    color: var(--card-white);
    font-weight: 300;
    font-size: 27px;
  }
  .contact__item {
    display: flex;
    align-items: center;
    gap: 10px;
    height: 38px;
  }
  .contact__icon { width: 26px; height: 26px; flex: none; }
</style>
</head>
<body>

<section class="card card--front">
  <svg class="card__shape" viewBox="0 0 660 426" aria-hidden="true">
    <defs>
      <filter id="tabShadowRed" x="-10%" y="-10%" width="120%" height="140%">
        <feDropShadow dx="0" dy="4" stdDeviation="5" flood-color="#5a0000" flood-opacity="0.7"/>
      </filter>
    </defs>
    <rect width="660" height="426" fill="var(--brand-red)"/>
    <path filter="url(#tabShadowRed)" fill="var(--card-white)"
      d="M0,0 H660 V85 H495 C470,85 460,95 445,120 L420,160 C405,180 395,190 370,190 H145 C125,190 115,185 105,165 L80,120 C65,95 55,85 25,85 H0 Z"/>
  </svg>
  <div class="brand">
    <span class="brand__dot"></span>
    <span class="brand__name">BRIGHTKETTLE.IE</span>
  </div>
  <ul class="contact">
    <li class="contact__item">
      <svg class="contact__icon" viewBox="0 0 26 26" aria-hidden="true">
        <circle cx="13" cy="13" r="12.5" fill="#fff"/>
        <g fill="none" stroke="#222" stroke-width="1.2">
          <circle cx="13" cy="13" r="8"/>
          <ellipse cx="13" cy="13" rx="3.5" ry="8"/>
          <line x1="5" y1="13" x2="21" y2="13"/>
          <line x1="6.5" y1="9" x2="19.5" y2="9"/>
          <line x1="6.5" y1="17" x2="19.5" y2="17"/>
        </g>
      </svg>
      <span>www.brightkettle.ie</span>
    </li>
    <li class="contact__item">
      <svg class="contact__icon" viewBox="0 0 26 26" aria-hidden="true">
        <circle cx="13" cy="13" r="12.5" fill="#fff"/>
        <g fill="none" stroke="#222" stroke-width="1.3">
          <rect x="6" y="8.5" width="14" height="9"/>
          <path d="M6,8.5 L13,14 L20,8.5 M6,17.5 L11,12.5 M20,17.5 L15,12.5"/>
        </g>
      </svg>
      <span>info@brightkettle.ie</span>
    </li>
  </ul>
</section>

<section class="card card--back">
  <svg class="card__shape" viewBox="0 0 660 426" aria-hidden="true">
    <defs>
      <linearGradient id="greyFade" x1="0" y1="0" x2="0" y2="1">
        <stop offset="0.15" stop-color="var(--grey-top)"/>
        <stop offset="1" stop-color="var(--grey-bottom)"/>
      </linearGradient>
      <filter id="tabShadowGrey" x="-10%" y="-10%" width="120%" height="140%">
        <feDropShadow dx="0" dy="4" stdDeviation="5" flood-color="#000" flood-opacity="0.6"/>
      </filter>
    </defs>
    <rect width="660" height="426" fill="url(#greyFade)"/>
    <path filter="url(#tabShadowGrey)" fill="var(--card-white)"
      d="M0,0 H660 V85 H495 C470,85 460,95 445,120 L420,160 C405,180 395,190 370,190 H145 C125,190 115,185 105,165 L80,120 C65,95 55,85 25,85 H0 Z"/>
  </svg>
  <div class="brand">
    <span class="brand__dot"></span>
    <span class="brand__name">BRIGHTKETTLE.IE</span>
  </div>
  <ul class="contact">
    <li class="contact__item">
      <svg class="contact__icon" viewBox="0 0 26 26" aria-hidden="true">
        <circle cx="13" cy="13" r="12.5" fill="#fff"/>
        <g fill="none" stroke="var(--brand-red)" stroke-width="1.3">
          <circle cx="13" cy="13" r="8"/>
          <ellipse cx="13" cy="13" rx="3.5" ry="8"/>
          <line x1="5" y1="13" x2="21" y2="13"/>
          <line x1="6.5" y1="9" x2="19.5" y2="9"/>
          <line x1="6.5" y1="17" x2="19.5" y2="17"/>
        </g>
      </svg>
      <span>www.brightkettle.ie</span>
    </li>
    <li class="contact__item">
      <svg class="contact__icon" viewBox="0 0 26 26" aria-hidden="true">
        <circle cx="13" cy="13" r="12.5" fill="#fff"/>
        <g fill="none" stroke="var(--brand-red)" stroke-width="1.4">
          <rect x="6" y="8.5" width="14" height="9"/>
          <path d="M6,8.5 L13,14 L20,8.5 M6,17.5 L11,12.5 M20,17.5 L15,12.5"/>
        </g>
      </svg>
      <span>info@brightkettle.ie</span>
    </li>
  </ul>
</section>

</body>
</html>
```